Web design - holistic filmmaker

I need a design for my new website.

I am a holistic filmmaker, ie I make films for healers, alternative practitioners, spiritual people and institutions that offer training in this field.

The design should be noble, bright, convey the feeling of space and expanse and have some particularly beautiful color accents.

The structure is: start page, offer, references, about me, imprint.

As an idea for the start page, I thought that either I could introduce myself as a filmmaker and my offer, or we could start right on the start page with the references, ie photos and links to already realized projects.

If you want more information or an exchange, I'd love to hear from you. At the moment I just don't know how to describe it better.

The winner will then be asked to design a logo.

Target Market(s)

healers, alternative practitioners, spiritual people and institutions that offer training in this field

Industry/Entity Type

Film production

Number of Pages Required

3 page

```html
<!DOCTYPE html>
<html lang="en">
<head>
<meta charset="utf-8">
<title>Holistic Filmmaker</title>
<link href="https://fonts.googleapis.com/css2?family=Inter:wght@400;500;600;700&display=swap" rel="stylesheet">
<style>
:root{
  --accent:#4b50b6;
  --accent-soft:#d8d7ef;
  --ink:#17202a;
  --body:#5b5f66;
  --white:#ffffff;
  --line:#b9b9c4;
}
*{margin:0;padding:0;box-sizing:border-box}
html,body{width:679px;height:1200px;overflow:hidden;background:var(--white)}
body{font-family:'Inter',sans-serif;color:var(--ink)}
.stage{width:679px;height:1200px;overflow:hidden;position:relative}
.page{position:absolute;left:0;top:0;width:1456px;height:2573px;transform:scale(0.46635);transform-origin:0 0}
.abs{position:absolute}
.dash{position:absolute;border:2px dashed var(--accent);border-radius:14px}
.logo{font-weight:700;font-size:44px;letter-spacing:-0.5px}
.nav{left:641px;top:64px;display:flex;gap:23px;font-size:14px;font-weight:600;text-transform:uppercase}
.nav .active{color:var(--accent)}
.btn{background:var(--accent);color:var(--white);font-weight:600;display:flex;align-items:center;justify-content:center;text-transform:uppercase;letter-spacing:.6px}
.btn-nav{left:1017px;top:46px;width:154px;height:51px;border-radius:12px;font-size:14px}
.photo{position:absolute;border-radius:14px}
.hero-title{left:284px;top:266px;font-size:72px;font-weight:700;line-height:68px;letter-spacing:-0.5px}
.search-back{left:260px;top:550px;width:113px;height:117px;background:var(--accent-soft);border-radius:14px}
.search{left:284px;top:526px;width:587px;height:115px;background:var(--white);border-radius:14px;box-shadow:0 24px 60px rgba(40,40,80,.10)}
.field{position:absolute;top:48px;display:flex;align-items:center;gap:8px;font-size:15px;font-weight:500;letter-spacing:.4px}
.divider{position:absolute;left:204px;top:48px;width:1px;height:20px;background:var(--line)}
.btn-search{position:absolute;left:423px;top:32px;width:131px;height:51px;border-radius:6px;font-size:13px}
.about-block{left:264px;top:1280px;width:152px;height:181px;background:var(--accent);border-radius:14px}
.thumb{left:628px;top:1273px;width:181px;height:215px;background:var(--white);padding:8px;border-radius:4px}
.h2{font-size:30px;font-weight:500;line-height:34px}
.bar{position:absolute;height:4px;width:52px;background:var(--accent);border-radius:2px}
.copy{font-size:12.6px;line-height:19px;color:var(--body)}
.news-title{left:0;width:1456px;top:1690px;text-align:center}
.news-sub{left:538px;width:380px;top:1728px;text-align:center}
.card{position:absolute;top:1843px;width:281px;height:396px;border:1.5px dashed var(--line);border-radius:14px}
.card-img{position:absolute;left:18px;top:16px;width:245px;height:159px;border-radius:6px}
.card-title{position:absolute;left:20px;top:197px;font-size:14.2px;font-weight:600;line-height:20px;white-space:nowrap}
.card-date{position:absolute;left:20px;top:245px;font-size:9px;color:var(--accent);font-weight:500}
.card-text{position:absolute;left:20px;top:270px;font-size:10.6px;line-height:18px;color:var(--body);white-space:nowrap}
.btn-card{position:absolute;left:20px;top:338px;width:86px;height:27px;border-radius:6px;font-size:8px;font-weight:700}
.footer{left:0;top:2342px;width:1456px;height:231px;background:var(--accent);color:var(--white)}
.footer h4{font-size:15px;font-weight:700;text-transform:uppercase}
.footer ul{list-style:none;font-size:13px;line-height:23px}
</style>
</head>
<body>
<div class="stage">
<div class="page">

  <div class="dash" style="left:-20px;top:-20px;width:163px;height:187px"></div>
  <div class="dash" style="left:1411px;top:45px;width:80px;height:115px"></div>

  <div class="abs logo" style="left:268px;top:52px">Logo</div>
  <nav class="abs nav">
    <span class="active">Home</span><span>About</span><span>Portfolio</span><span>Blog</span><span>Contact</span>
  </nav>
  <div class="abs btn btn-nav">Get a quote</div>

  <div class="dash" style="left:671px;top:128px;width:117px;height:116px"></div>
  <div class="dash" style="left:1023px;top:540px;width:176px;height:207px"></div>
  <div class="photo" style="left:695px;top:151px;width:476px;height:565px;background:linear-gradient(160deg,#cfc3c8 0%,#8d7c86 35%,#9d3a35 65%,#2b2c31 100%)" role="img" aria-label="Filmmaker operating a camera on a rooftop film set at dusk"></div>

  <h1 class="abs hero-title">Holistic<br>Filmmaker</h1>

  <div class="abs search-back"></div>
  <div class="abs search">
    <div class="field" style="left:42px">
      <svg width="16" height="16" viewBox="0 0 16 16" fill="none" stroke="#4b50b6" stroke-width="1.5"><circle cx="7" cy="7" r="5.5"/><path d="M11 11l4 4"/></svg>
      Type Job title
    </div>
    <div class="divider"></div>
    <div class="field" style="left:229px">
      <svg width="16" height="20" viewBox="0 0 16 20" fill="none" stroke="#4b50b6" stroke-width="1.4"><path d="M8 19s6.5-6.5 6.5-11A6.5 6.5 0 0 0 1.5 8C1.5 12.5 8 19 8 19z"/><circle cx="8" cy="8" r="2.4"/></svg>
      Location
    </div>
    <div class="btn btn-search">Get a quote</div>
  </div>

  <div class="dash" style="left:52px;top:651px;width:57px;height:57px"></div>
  <div class="dash" style="left:67px;top:667px;width:58px;height:56px"></div>

  <div class="dash" style="left:257px;top:905px;width:175px;height:207px"></div>
  <div class="abs about-block"></div>
  <div class="photo" style="left:285px;top:929px;width:432px;height:512px;background:linear-gradient(150deg,#3f4a2a 0%,#6d6a58 40%,#2a2b2e 100%)" role="img" aria-label="Portrait of the filmmaker holding a camera"></div>
  <div class="abs thumb">
    <div style="width:165px;height:199px;background:linear-gradient(160deg,#d9d9d6 0%,#8a8886 45%,#d98a2a 80%,#4a4a4a 100%)" role="img" aria-label="Small portrait of the filmmaker"></div>
  </div>

  <h2 class="abs h2" style="left:791px;top:960px;width:380px">Lorem Ipsum is simply dummy text of the printing</h2>
  <div class="bar" style="left:792px;top:1049px"></div>
  <p class="abs copy" style="left:792px;top:1069px;width:370px">There are many variations of passages of Lorem Ipsum available, but the majority have suffered alteration in some form, by injected humour, or randomised words which don't look even slightly believable.</p>
  <p class="abs copy" style="left:792px;top:1164px;width:370px">If you are going to use a passage of Lorem Ipsum, you need to be sure there isn't anything embarrassing hidden in the middle of text.</p>

  <div class="abs" style="left:843px;top:1281px;width:61px;height:61px;border-radius:50%;background:var(--ink)"></div>
  <p class="abs copy" style="left:845px;top:1352px;width:295px">There are many variations of passages of Lorem Ipsum available, but the majority have suffered alteration in some form.</p>
  <div class="abs" style="left:845px;top:1424px;width:210px;border-top:1px dashed var(--line)"></div>
  <div class="abs" style="left:843px;top:1438px;font-size:15px;color:#333">Dara Velmont</div>
  <div class="abs" style="left:844px;top:1459px;font-size:11px;color:#333">Hade Of Idea</div>

  <h2 class="abs h2 news-title">Recent News Post</h2>
  <p class="abs copy news-sub">Sed ut perspiciatis unde omnis iste natus error sit voluaccusan doloremque laudantium.</p>
  <div class="bar" style="left:702px;top:1777px"></div>

  <article class="card" style="left:284px">
    <div class="card-img" style="background:var(--accent)" role="img" aria-label="News post image"></div>
    <h3 class="card-title">If you use this site regularly<br>and would like to.</h3>
    <p class="card-text">There are many variations of passages of<br>Lorem Ipsum available, but the majority<br>have suffered alteration.</p>
    <div class="btn btn-card">Read more</div>
  </article>
  <article class="card" style="left:588px">
    <div class="card-img" style="background:var(--ink)" role="img" aria-label="News post image"></div>
    <h3 class="card-title">There are many variations of<br>passages of Lorem.</h3>
    <div class="card-date">JUNE 10, 2021</div>
    <p class="card-text">There are many variations of passages of<br>Lorem Ipsum available, but the majority<br>have suffered alteration.</p>
    <div class="btn btn-card">Read more</div>
  </article>
  <article class="card" style="left:891px">
    <div class="card-img" style="background:var(--ink)" role="img" aria-label="News post image"></div>
    <h3 class="card-title">At vero eos et accusamus et<br>iusto odio dignissimos ducimus.</h3>
    <div class="card-date">JUNE 10, 2021</div>
    <p class="card-text">There are many variations of passages of<br>Lorem Ipsum available, but the majority<br>have suffered alteration.</p>
    <div class="btn btn-card">Read more</div>
  </article>

  <footer class="abs footer">
    <div class="abs logo" style="left:282px;top:58px">Logo</div>
    <p class="abs" style="left:284px;top:122px;width:290px;font-size:13px;line-height:20px">Contrary to popular belief, Lorem<br>Ipsum is not simply random text. It has roots in a<br>piece of classical.</p>
    <h4 class="abs" style="left:663px;top:92px">Our Company</h4>
    <ul class="abs" style="left:663px;top:123px"><li>• About Us</li><li>• Product</li><li>• Pricing</li></ul>
    <ul class="abs" style="left:776px;top:123px"><li>• FAQ</li><li>• Contact us</li><li>• Blog</li></ul>
    <h4 class="abs" style="left:963px;top:92px">Get in touch</h4>
    <ul class="abs" style="left:965px;top:125px;line-height:21px"><li>P. 555 014 207 300</li><li>E. HELLO@LUMENFRAME.COM</li><li>W. LUMENFRAME.COM</li></ul>
  </footer>

</div>
</div>
</body>
</html>
```